Consulting company with focus on aviation needs

We need a new business card design for our company. The company consults with multiple players in the industry like manufacturers and airlines. It is also a supplier and an inter-company level. Given the targeted industry (aviation) it should be both kind of serious, sound, secure, classy, ​​but also a bit technical, innovative. Should not be too playful, however, "fresh", "airy", "ligth" and "suprising" are suitabe attributes. The existing logo shall be used.

Industry/Entity Type

Airlines

```html
<!DOCTYPE html>
<html lang="en">
<head>
<meta charset="utf-8">
<title>Ventara business card</title>
<link rel="stylesheet" href="https://fonts.googleapis.com/css2?family=Michroma&family=Ubuntu:wght@400;500&display=swap">
<style>
  :root {
    --backdrop: #e4e4e4;
    --card-light: #ffffff;
    --card-dark: #3a3a3c;
    --brand-grey: #6d6e70;
    --brand-orange: #f39a31;
    --band-orange: #f28a2f;
    --brand-teal: #2ba58c;
    --text-light: #ffffff;
  }
  * { margin: 0; padding: 0; box-sizing: border-box; }
  html, body { width: 1200px; height: 801px; overflow: hidden; }
  body {
    position: relative;
    background: var(--backdrop);
    font-family: "Ubuntu", sans-serif;
  }
  .card {
    position: absolute;
    top: 273px;
    width: 448px;
    height: 255px;
    border-radius: 18px;
    overflow: hidden;
  }
  .card--front { left: 133px; background: var(--card-light); }
  .card--back { left: 620px; background: var(--card-dark); }

  .brand-mark {
    position: absolute;
    border-radius: 50%;
    background: var(--brand-teal);
  }
  .card--front .brand-mark { left: 185px; top: 48px; width: 78px; height: 78px; }
  .card--back .brand-mark { left: 84px; top: 9px; width: 50px; height: 50px; }

  .brand-name {
    position: absolute;
    font-family: "Michroma", sans-serif;
    font-weight: 400;
    letter-spacing: 0.12em;
    line-height: 1;
  }
  .card--front .brand-name {
    left: 0; width: 100%; text-align: center;
    top: 150px; font-size: 30px; color: var(--brand-grey);
  }
  .card--back .brand-name {
    left: 33px; top: 70px; font-size: 19px; color: var(--text-light);
  }
  .tagline {
    position: absolute;
    color: var(--brand-orange);
    white-space: nowrap;
  }
  .card--front .tagline {
    left: 0; width: 100%; text-align: center;
    top: 185px; font-size: 13.5px;
  }
  .card--back .tagline { left: 33px; top: 92px; font-size: 9.5px; }

  .title-band {
    position: absolute;
    left: 0; top: 110px;
    width: 258px; height: 39px;
    background: var(--band-orange);
    color: var(--text-light);
    font-size: 12.5px;
    line-height: 15px;
    padding: 5px 0 0 40px;
  }
  .contact-list {
    position: absolute;
    left: 33px; top: 160px;
    list-style: none;
  }
  .contact-list li {
    display: flex;
    align-items: center;
    height: 20.5px;
    color: var(--text-light);
    font-size: 12px;
  }
  .contact-list svg { width: 11px; height: 11px; margin-right: 7px; }
  .feature-disc {
    position: absolute;
    left: 262px; top: 38px;
    width: 206px; height: 206px;
    border-radius: 50%;
    background: var(--brand-teal);
  }
</style>
</head>
<body>
  <section class="card card--front">
    <div class="brand-mark"></div>
    <div class="brand-name">VENTARA</div>
    <div class="tagline">Linking Partners - Shaping Routes</div>
  </section>

  <section class="card card--back">
    <div class="brand-mark"></div>
    <div class="brand-name">VENTARA</div>
    <div class="tagline">Linking Partners - Shaping Routes</div>
    <div class="title-band">
      <div class="person-name">Name</div>
      <div class="person-role">Designation</div>
    </div>
    <ul class="contact-list">
      <li>
        <svg viewBox="0 0 12 12"><circle cx="6" cy="6" r="6" fill="#f39a31"/><path d="M3.6 3.2l1.2-.2.7 1.6-.8.6q.6 1.3 1.9 1.9l.6-.8 1.6.7-.2 1.2Q5.5 8.4 3.6 3.2z" fill="#3a3a3c"/></svg>
        xxxxxxxxx
      </li>
      <li>
        <svg viewBox="0 0 12 12"><circle cx="6" cy="6" r="6" fill="#f39a31"/><path d="M6 2.5a2.2 2.2 0 0 1 2.2 2.2C8.2 6.4 6 9.5 6 9.5S3.8 6.4 3.8 4.7A2.2 2.2 0 0 1 6 2.5z" fill="#3a3a3c"/><circle cx="6" cy="4.7" r=".8" fill="#f39a31"/></svg>
        xxxxxxxxx
      </li>
      <li>
        <svg viewBox="0 0 12 12"><circle cx="6" cy="6" r="6" fill="#f39a31"/><rect x="3" y="3.8" width="6" height="4.4" fill="none" stroke="#3a3a3c" stroke-width=".9"/><path d="M3 3.8l3 2.4 3-2.4" fill="none" stroke="#3a3a3c" stroke-width=".9"/></svg>
        xxxxx@ventara.com
      </li>
      <li>
        <svg viewBox="0 0 12 12"><circle cx="6" cy="6" r="6" fill="#f39a31"/><circle cx="6" cy="6" r="3" fill="none" stroke="#3a3a3c" stroke-width=".8"/><path d="M3 6h6M6 3q-1.6 3 0 6M6 3q1.6 3 0 6" fill="none" stroke="#3a3a3c" stroke-width=".7"/></svg>
        www.ventara.com
      </li>
    </ul>
    <div class="feature-disc"></div>
  </section>
</body>
</html>
```